Business Card Design Project

Use newly designed logo and tie into newly designed website
I need a new logo and website layout designed for my partner's business. This is a birthday present. His business is interior painting, wallpapering and design. He also has access to a wide variety of products including carpet, fabrics, furniture, wallpaper, tile, countertops, etc. I have attached some screen shots of his website for reference. He is a one man shop and has a stellar reputation with his customers. He is on-time, very tidy, excellent with animals, and always finishes on time and on budget. There are no restrictions on colors or fonts. The logo needs to work well with the website, business cards and printed materials. The website needs to flow content for device size so it looks just as good on a cell phone or tablet as it does on a desktop computer. Whatever the heck that's called!Thanks. I am looking forward to seeing everyone's ideas.
Updates
Hi Designers,
Please refer to the uploaded files and make use of either Horizontal or Vertical versions of the logo depending on what you think is suitable for your design proposals.
We look forward to your creative submissions!
Target Market(s)
Consumers looking to improve the interior environment of their homes by updating wall paint or paper, flooring (either carpet, tile, or hardwoods), counter tops, window treatments, etc. Clients tend to be more upper middle class and have certain taste levels and expectations. New logo, website and business card should align to meet those levels.
Industry/Entity Type
Cell Phone
Look and feel
Each slider illustrates characteristics of the customer's brand and the style your logo design should communicate.

```html
<!DOCTYPE html>
<html lang="en">
<head>
<meta charset="utf-8">
<title>Verano Interior Designs – Business Card</title>
<link rel="stylesheet" href="https://fonts.googleapis.com/css2?family=Cinzel:wght@400;500&family=Open+Sans:wght@400;600&display=swap">
<style>
  :root {
    --backdrop: #ebe6de;
    --card: #ffffff;
    --plum: #3b2461;
    --crimson: #a3232c;
    --sand: #c7bb92;
    --saffron: #f1ab1e;
    --ink: #3a3a3a;
    --muted: #6b6b6b;
  }
  * { box-sizing: border-box; margin: 0; padding: 0; }
  html, body { width: 1200px; height: 1023px; overflow: hidden; }
  body { background: var(--backdrop); position: relative; font-family: "Open Sans", Arial, sans-serif; }

  .business-card {
    position: absolute; left: 75px; top: 211px;
    width: 1050px; height: 600px;
    background: var(--card);
    box-shadow: 0 14px 40px rgba(60, 45, 25, 0.22);
    overflow: hidden;
  }

  .brand-block {
    position: absolute; left: 70px; top: 0; width: 420px; height: 600px;
    display: flex; align-items: center; gap: 26px;
  }
  .brand-square { width: 46px; height: 46px; background: var(--saffron); flex: none; }
  .brand-name {
    font-family: "Cinzel", Georgia, serif; font-weight: 400; color: var(--plum);
    line-height: 1.05;
  }
  .brand-name .primary { display: block; font-size: 62px; letter-spacing: 2px; }
  .brand-name .secondary { display: block; font-size: 24px; letter-spacing: 3px; margin-top: 6px; }

  .icon-rail { position: absolute; left: 520px; top: 0; width: 40px; height: 600px; background: var(--plum); }
  .icon-rail svg { position: absolute; left: 6px; width: 28px; height: 28px; }

  .person { position: absolute; left: 585px; top: 40px; width: 390px; }
  .person-name { font-family: "Cinzel", Georgia, serif; font-size: 36px; color: var(--crimson); letter-spacing: 1px; }
  .person-title { position: absolute; right: 0; top: -4px; font-size: 22px; color: var(--muted); }

  .contact-list { position: absolute; left: 585px; top: 160px; list-style: none; font-size: 21px; color: var(--ink); }
  .contact-list li { height: 32px; line-height: 32px; }

  .web-band {
    position: absolute; left: 560px; top: 300px; width: 400px; height: 58px;
    background: var(--sand); color: #fff; font-size: 21px;
    display: flex; align-items: center; justify-content: center; letter-spacing: 0.5px;
  }
  .edge-band { position: absolute; right: 0; top: 0; width: 50px; height: 440px; background: var(--crimson); }
  .address-band {
    position: absolute; left: 560px; top: 440px; width: 490px; height: 160px;
    background: var(--saffron); color: #fff; font-size: 21px; letter-spacing: 0.5px;
    padding: 40px 0 0 50px; line-height: 38px;
  }
</style>
</head>
<body>
  <main class="business-card">
    <section class="brand-block">
      <span class="brand-square" aria-hidden="true"></span>
      <h1 class="brand-name">
        <span class="primary">VERANO</span>
        <span class="secondary">INTERIOR DESIGNS</span>
      </h1>
    </section>

    <div class="icon-rail" aria-hidden="true">
      <svg style="top:162px" viewBox="0 0 28 28"><circle cx="14" cy="14" r="12" fill="#fff"/><path d="M9 8c1-1 2-1 3 0l1 2c0 1 0 1-1 2 1 2 2 3 4 4 1-1 1-1 2-1l2 1c1 1 1 2 0 3-2 2-5 1-8-2s-4-6-3-9z" fill="#3b2461"/></svg>
      <svg style="top:194px" viewBox="0 0 28 28"><circle cx="14" cy="14" r="12" fill="#fff"/><path d="M9 8c1-1 2-1 3 0l1 2c0 1 0 1-1 2 1 2 2 3 4 4 1-1 1-1 2-1l2 1c1 1 1 2 0 3-2 2-5 1-8-2s-4-6-3-9z" fill="#3b2461"/></svg>
      <svg style="top:226px" viewBox="0 0 28 28"><circle cx="14" cy="14" r="12" fill="#fff"/><rect x="7.5" y="9.5" width="13" height="9" fill="none" stroke="#3b2461" stroke-width="1.6"/><path d="M7.5 9.5l6.5 5 6.5-5" fill="none" stroke="#3b2461" stroke-width="1.6"/></svg>
    </div>

    <header class="person">
      <h2 class="person-name">MARCUS HALE</h2>
      <p class="person-title">Director</p>
    </header>

    <ul class="contact-list">
      <li>+852 55501234</li>
      <li>+852 55509876</li>
      <li>marcus.hale@verano.example</li>
    </ul>

    <div class="web-band">www.verano.example</div>
    <div class="edge-band" aria-hidden="true"></div>
    <address class="address-band" style="font-style:normal">
      5/F, HARBOURLINE HOUSE<br>
      18-22 LANTERN ROAD, KOWLOON POINT
    </address>
  </main>
</body>
</html>
```